Lobby Wardens Staffing

Lobby wardens is similar to a security company but is more concierge/customer service oriented. Picture a security guard in a suit working at a condo or office building. Our thoughts for a logo is a silhouette of a male/female sitting at a desk or some type of crest but were open to creative ideas.

Target Market(s)

Property Managers

Industry/Entity Type

Security

Font styles to use
Serif

Requirements
Must have
• Male/Female sitting professionally at a desk.
Nice to have
• Vertical card
Should not have
• Cartoons

```html
<!DOCTYPE html>
<html lang="en">
<head>
<meta charset="utf-8">
<title>Lobby Wardens Staffing – Business Card</title>
<link href="https://fonts.googleapis.com/css2?family=Open+Sans:wght@400;600;700&display=swap" rel="stylesheet">
<style>
  :root {
    --backdrop: #e9e6e1;
    --card-white: #ffffff;
    --card-shade: #eeeeee;
    --header-black: #111214;
    --accent-blue: #1f97d4;
    --band-blue: #2a8fcb;
    --band-blue-light: #4fb3e6;
    --ink: #1a1a1a;
    --ink-soft: #333333;
    --silhouette: #3b3c3e;
    --silhouette-light: #6a6b6d;
  }
  * { margin: 0; padding: 0; box-sizing: border-box; }
  html, body {
    width: 1200px;
    height: 1023px;
    overflow: hidden;
    background: var(--backdrop);
    font-family: "Open Sans", Arial, sans-serif;
  }
  .business-card {
    position: absolute;
    left: 375px;
    top: 112px;
    width: 450px;
    height: 800px;
    background: linear-gradient(180deg, var(--card-white) 0%, var(--card-shade) 100%);
    box-shadow: 0 10px 30px rgba(0,0,0,0.18);
    overflow: hidden;
  }
  .card-header {
    position: absolute;
    left: 0; top: 0;
    width: 100%;
    height: 190px;
    background: var(--header-black);
    border-bottom: 6px solid var(--accent-blue);
    display: flex;
    align-items: center;
    justify-content: center;
    gap: 14px;
    padding: 0 28px;
  }
  .brand-dot {
    width: 22px;
    height: 22px;
    border-radius: 50%;
    background: var(--accent-blue);
    flex: none;
  }
  .brand-name {
    color: var(--card-white);
    font-weight: 700;
    font-size: 26px;
    letter-spacing: 1px;
    text-transform: uppercase;
    white-space: nowrap;
  }
  .contact-block {
    position: absolute;
    top: 232px;
    width: 100%;
    text-align: center;
  }
  .person-name {
    color: var(--accent-blue);
    font-weight: 700;
    font-size: 28px;
    letter-spacing: 0.5px;
    text-transform: uppercase;
  }
  .person-title {
    color: var(--ink-soft);
    font-size: 14px;
    letter-spacing: 1px;
    text-transform: uppercase;
    margin-top: 2px;
  }
  .person-phone, .person-email {
    color: var(--ink);
    font-size: 21px;
    line-height: 30px;
  }
  .person-phone { margin-top: 16px; }
  .desk-figure {
    position: absolute;
    left: 70px;
    top: 430px;
    width: 340px;
    height: 250px;
    border-radius: 120px 120px 0 0;
    background: linear-gradient(180deg, var(--silhouette-light) 0%, var(--silhouette) 60%);
  }
  .card-footer {
    position: absolute;
    left: 0; bottom: 0;
    width: 100%;
    height: 120px;
    background: linear-gradient(180deg, var(--band-blue) 0%, var(--band-blue-light) 100%);
  }
  .website {
    position: absolute;
    right: 28px;
    top: 14px;
    color: var(--ink);
    font-size: 17px;
    letter-spacing: 0.3px;
  }
</style>
</head>
<body>
  <div class="business-card">
    <header class="card-header">
      <span class="brand-dot"></span>
      <span class="brand-name">Lobby Wardens Staffing</span>
    </header>
    <section class="contact-block">
      <div class="person-name">Dan Marchetti</div>
      <div class="person-title">Director</div>
      <div class="person-phone">555-014-2290</div>
      <div class="person-email">DanMarchetti@mailbox.com</div>
    </section>
    <div class="desk-figure" role="img" aria-label="Dark silhouette of a professional seated at a desk, speaking on a corded telephone"></div>
    <footer class="card-footer">
      <span class="website">www.lobbywardensstaffing.com</span>
    </footer>
  </div>
</body>
</html>
```